Global recruitment firm needs a design for marketing material

We need a design for our company Harlow Crest, which is a global recruitment firm specializing in senior finance and executive positions. This will be a template/ background for all our marketing material. We are looking to communicate a consistent message to current and existing clients. Uploaded below are our files describing our mission, values and strategy and story. Please also look at our website www.harlowcrest-demo.com.au. Examples of where this design will be used will be in client proposals, marketing info telling our story, social media content, infographics, and general client communication.

Target Market(s)

Client companies in the finance industry, Executive level finance candidates(CEO, CFO)

Requirements
Must have
• company logo, mission, value, strategy, website, our story
• Will be using the graphic for website, all communication with clients > looking for something to use for different purposes

```html
<!DOCTYPE html>
<html lang="en">
<head>
<meta charset="utf-8">
<title>Harlow Crest – Connecting Talent With Opportunity Globally</title>
<link rel="stylesheet" href="https://fonts.googleapis.com/css2?family=Mulish:wght@400;600;700;800&family=Oswald:wght@500&display=swap">
<style>
  :root {
    --brand-blue: #1c72b8;
    --brand-navy: #1d4f86;
    --band-blue: #4b8fe8;
    --strategy-yellow: #f7b93c;
    --strategy-green: #37bb95;
    --strategy-blue: #4a85de;
    --story-yellow: #fcc53f;
    --card-grey: #ececec;
    --ink: #2b2b2b;
    --ink-soft: #6a6a6a;
    --white: #ffffff;
    --footer-bg: #3a3a3a;
    --footer-label: #4592e6;
    --footer-text: #e6e6e6;
    --footer-line: #8a8a8a;
  }
  * { box-sizing: border-box; margin: 0; padding: 0; }
  html, body { width: 1200px; height: 3416px; overflow: hidden; background: var(--white); }
  body { position: relative; font-family: "Mulish", sans-serif; color: var(--ink); }

  .logo { position: absolute; left: 68px; top: 78px; display: flex; align-items: center; gap: 16px; }
  .logo-mark { width: 40px; height: 40px; background: var(--brand-blue); }
  .logo-name { font-size: 40px; font-weight: 800; color: var(--brand-navy); letter-spacing: 1px; }

  .call-us { position: absolute; right: 85px; top: 66px; font-size: 37px; font-weight: 700; color: var(--brand-blue); display: flex; align-items: center; gap: 12px; }
  .call-us .number { color: var(--ink); font-weight: 600; }
  .call-us svg { width: 36px; height: 36px; }

  .hero-photo { position: absolute; left: 75px; top: 182px; width: 1057px; height: 440px;
    background: radial-gradient(ellipse at 50% 60%, #e9d2c3 0%, #cfb3a3 35%, #f4f2f1 75%); }

  .hero-banner { position: absolute; left: 84px; top: 622px; width: 1038px; height: 291px; background: var(--brand-blue);
    display: flex; align-items: center; justify-content: center; text-align: center;
    color: var(--white); font-size: 54px; font-weight: 700; line-height: 1.27; }

  .section-title { position: absolute; left: 0; width: 1200px; text-align: center; font-size: 36px; font-weight: 700; }
  .strategy-title { top: 980px; color: var(--ink); }

  .strategy-card { position: absolute; top: 1097px; width: 278px; height: 310px; border-radius: 22px 60px 22px 60px;
    background: var(--card-grey); box-shadow: 6px 6px 0 #d4d4d4; overflow: hidden; }
  .strategy-card .shape { position: absolute; inset: 0; }
  .strategy-card .label { position: absolute; left: 40px; top: 38px; font-family: "Oswald", sans-serif; font-weight: 500;
    color: var(--white); font-size: 38px; line-height: 1.2; text-align: center; }
  .strategy-card .icon { position: absolute; right: 28px; bottom: 28px; width: 112px; height: 112px; }
  .card-engage { left: 137px; }
  .card-challenge { left: 464px; }
  .card-select { left: 792px; }

  .story-band { position: absolute; left: 84px; top: 1489px; width: 1038px; height: 430px; background: var(--story-yellow); }
  .story-photo { position: absolute; left: 137px; top: 1548px; width: 312px; height: 308px; }
  .story-text { position: absolute; left: 503px; top: 1538px; width: 600px; color: var(--white); }
  .block-heading { font-size: 36px; font-weight: 700; margin-bottom: 22px; }
  .block-body { font-size: 27px; line-height: 43px; white-space: nowrap; }

  .mission-text { position: absolute; left: 137px; top: 1970px; width: 580px; }
  .mission-text .block-heading { color: #3a3a3a; }
  .mission-text .block-body { color: var(--ink-soft); font-size: 27px; line-height: 42px; }
  .mission-photo { position: absolute; left: 756px; top: 1981px; width: 310px; height: 310px; }

  .value-band { position: absolute; left: 84px; top: 2352px; width: 1038px; height: 542px; background: var(--band-blue); }
  .value-title { top: 2404px; color: var(--white); }
  .value-body { position: absolute; left: 84px; top: 2476px; width: 1038px; text-align: center; color: var(--white); font-size: 27px; line-height: 38px; white-space: nowrap; }
  .value-devices { position: absolute; left: 182px; top: 2642px; width: 813px; height: 360px;
    background: linear-gradient(180deg, #3c3c3c 0%, #5a5a5a 55%, #d9dde2 100%); border-radius: 14px; }

  .footer { position: absolute; left: 0; top: 3088px; width: 1200px; height: 328px; background: var(--footer-bg); color: var(--footer-text); }
  .footer-contacts { position: absolute; top: 64px; width: 100%; text-align: center; font-size: 29px; }
  .footer-contacts .label { color: var(--footer-label); font-weight: 700; }
  .footer-contacts .gap { display: inline-block; width: 40px; }
  .footer-divider { position: absolute; top: 158px; width: 100%; height: 1px; }
  .footer-divider .line { position: absolute; top: 0; height: 2px; background: var(--footer-line); }
  .social { position: absolute; top: 136px; left: 517px; display: flex; gap: 12px; }
  .social span { width: 46px; height: 46px; border-radius: 50%; background: #9a9a9a; }
  .social span.active { background: #3a8fe0; }
  .footer-legal { position: absolute; top: 220px; width: 100%; text-align: center; font-size: 29px; }
  .footer-legal .sep { margin: 0 28px; }
</style>
</head>
<body>

<header>
  <div class="logo"><span class="logo-mark"></span><span class="logo-name">Harlow Crest</span></div>
  <div class="call-us">Call Us:
    <svg viewBox="0 0 24 24" aria-hidden="true"><path fill="#1c72b8" d="M6.6 10.8a15.2 15.2 0 0 0 6.6 6.6l2.2-2.2c.3-.3.7-.4 1-.2 1.1.4 2.3.6 3.6.6.6 0 1 .4 1 1V20c0 .6-.4 1-1 1A17 17 0 0 1 3 4c0-.6.4-1 1-1h3.5c.6 0 1 .4 1 1 0 1.2.2 2.4.6 3.6.1.3 0 .7-.2 1z"/></svg>
    <span class="number">+61 400-555-017</span></div>
</header>

<div class="hero-photo" role="img" aria-label="Photo of five smiling business professionals leaning in together"></div>
<div class="hero-banner">Connecting Talent<br>With Opportunity Globally</div>

<h2 class="section-title strategy-title">--&nbsp; Our Strategy &nbsp;--</h2>

<div class="strategy-card card-engage">
  <svg class="shape" viewBox="0 0 278 310" preserveAspectRatio="none" aria-hidden="true"><path fill="var(--strategy-yellow)" d="M0 0H215Q262 0 262 40Q210 150 150 210Q85 275 30 310H0Z"/></svg>
  <div class="label">01<br>Engage</div>
  <svg class="icon" viewBox="0 0 100 100" role="img" aria-label="Handshake icon"><rect x="10" y="40" width="80" height="24" rx="12" fill="var(--strategy-yellow)"/></svg>
</div>
<div class="strategy-card card-challenge">
  <svg class="shape" viewBox="0 0 278 310" preserveAspectRatio="none" aria-hidden="true"><path fill="var(--strategy-green)" d="M0 0H215Q262 0 262 40Q210 150 150 210Q85 275 30 310H0Z"/></svg>
  <div class="label">02<br>Challenge</div>
  <svg class="icon" viewBox="0 0 100 100" aria-hidden="true">
    <circle cx="50" cy="52" r="40" fill="none" stroke="var(--strategy-green)" stroke-width="9"/>
    <circle cx="50" cy="52" r="22" fill="none" stroke="var(--strategy-green)" stroke-width="9"/>
    <circle cx="50" cy="52" r="7" fill="var(--strategy-green)"/>
    <path d="M50 52L86 16M78 10l8 6 6 8" stroke="var(--strategy-green)" stroke-width="6" fill="none"/>
  </svg>
</div>
<div class="strategy-card card-select">
  <svg class="shape" viewBox="0 0 278 310" preserveAspectRatio="none" aria-hidden="true"><path fill="var(--strategy-blue)" d="M0 0H215Q262 0 262 40Q210 150 150 210Q85 275 30 310H0Z"/></svg>
  <div class="label">03<br>Select</div>
  <svg class="icon" viewBox="0 0 100 100" aria-hidden="true">
    <path d="M40 40L82 56 64 62 80 82 72 88 56 68 46 82Z" fill="var(--strategy-blue)"/>
    <path d="M34 34L22 22M40 26V10M26 40H10M48 30l8-12M30 48l-12 8" stroke="var(--strategy-blue)" stroke-width="4" stroke-linecap="round"/>
  </svg>
</div>

<section class="story-band"></section>
<svg class="story-photo" viewBox="0 0 312 308" role="img" aria-label="Photo of two business people shaking hands in an office">
  <defs><linearGradient id="storyTone" x1="0" y1="0" x2="1" y2="1"><stop offset="0" stop-color="#e8dccb"/><stop offset="1" stop-color="#8c8a86"/></linearGradient></defs>
  <path fill="url(#storyTone)" d="M60 20C130-10 260 0 300 80S290 280 190 300 20 290 5 190 0 45 60 20Z"/>
</svg>
<div class="story-text">
  <h3 class="block-heading">Our Story ----</h3>
  <p class="block-body">30 years of experience enables us to<br>partner with our clients to challenge the<br>recruitment strategy on people, positions<br>and the process, to build high perform-<br>ing finance teams ...</p>
</div>

<div class="mission-text">
  <h3 class="block-heading">Our Mission ----</h3>
  <p class="block-body">Harlow Crest is a global search firm<br>originating in Sydney in 2010 and today<br>partnering with finance professionals in<br>Australia, Hong Kong, Singapore, India,<br>London, United States and Canada ...</p>
</div>
<svg class="mission-photo" viewBox="0 0 310 310" role="img" aria-label="Photo of several hands joining coloured puzzle pieces">
  <defs><linearGradient id="missionTone" x1="0" y1="0" x2="1" y2="1"><stop offset="0" stop-color="#cfd6dd"/><stop offset=".5" stop-color="#6f7f8f"/><stop offset="1" stop-color="#3b4a5a"/></linearGradient></defs>
  <path fill="url(#missionTone)" d="M120 10C200-5 300 40 305 140S250 300 150 305 5 240 10 150 50 25 120 10Z"/>
</svg>

<section class="value-band"></section>
<h2 class="section-title value-title">-- Our Value --</h2>
<p class="value-body">There are many variations of passages of lorem site that<br>Lorem Ipsum available, but the majority have suffered alteration in<br>form, by injected humour then proud to be ...</p>
<div class="value-devices" role="img" aria-label="Illustration of the website shown on a desktop monitor, tablet and laptop"></div>

<footer class="footer">
  <p class="footer-contacts"><span class="label">Phone:</span> +61 400-555-017<span class="gap"></span><span class="label">Email:</span> hello@harlowcrest-demo.com.au</p>
  <div class="footer-divider">
    <span class="line" style="left:140px;width:344px"></span>
    <span class="line" style="left:716px;width:344px"></span>
  </div>
  <div class="social" aria-label="Social links"><span></span><span class="active"></span><span></span></div>
  <p class="footer-legal">© 2018 Harlow Crest.<span class="sep">|</span>www.harlowcrest-demo.com.au</p>
</footer>

</body>
</html>
```